mobile app maker needs website redone

We currently have a running website that generates some traffic and looks ok but now we want to revamp it with professional modern eye catching design.
We are open to proposals and open to any new ideas or suggestions but we have to see your previous work.
our current site is www.brivelapp.com

Industry/Entity Type

It Professional

Coding

Coded - Design and coding required

Number of Pages Required

5+ page

Font styles to use
Serif
Other font styles liked:
• open

Requirements
Must have
• modern look and feel easy to use
Nice to have
• responsive websites , example are as follow ,http://quonpage-template.sitemorra.io , dalvo.com , http://marpex.sitemorra.io

```html
<!DOCTYPE html>
<html lang="en">
<head>
<meta charset="utf-8">
<title>Brivel Marketing – Mobile Apps &amp; Mobile Websites</title>
<link rel="stylesheet" href="https://fonts.googleapis.com/css2?family=Open+Sans:ital,wght@0,300;0,400;0,600;0,700;1,400&display=swap">
<style>
:root{
  --blue:#2b5d9c;
  --blue-dark:#1d4a86;
  --hero-a:#1f4f8f;
  --hero-b:#5c8fc4;
  --green:#7cc142;
  --green-dark:#5fa82c;
  --grey-band:#e6ebef;
  --text:#333a40;
  --muted:#7d868e;
  --contact:#5f9acb;
  --footer:#2c5a9b;
  --map:#e7e3da;
  --white:#ffffff;
}
*{box-sizing:border-box;margin:0;padding:0}
html,body{width:1200px;height:3488px;overflow:hidden;background:var(--white)}
body{font-family:"Open Sans",sans-serif;color:var(--text)}
.canvas{position:relative;width:1200px;height:3488px;overflow:hidden}
.bands{position:absolute;left:0;top:0}
.abs{position:absolute}

/* nav */
.brand{left:130px;top:22px;display:flex;align-items:center;gap:12px;color:var(--white);font-size:26px;font-weight:600}
.brand-dot{width:30px;height:30px;border-radius:50%;background:var(--white)}
.nav{right:0;top:0;display:flex;height:80px}
.nav a{position:absolute;top:32px;color:var(--white);font-size:15px;text-decoration:none;white-space:nowrap}
.nav a.active{padding-bottom:24px;border-bottom:2px solid var(--green)}

/* hero */
.hero-title{left:130px;top:180px;color:var(--white);font-size:44px;font-weight:700;line-height:60px}
.hero-title .accent{color:var(--green)}
.hero-text{left:130px;top:318px;width:560px;color:var(--white);font-size:14px;line-height:22px}
.btn-outline{display:flex;align-items:center;justify-content:center;gap:8px;border:2px solid var(--green);color:var(--white);font-size:14px;height:38px}
.login{left:130px;top:393px;width:128px}
.lock{width:10px;height:9px;background:var(--white);border-radius:2px;position:relative}
.hero-visual{left:630px;top:95px;width:440px;height:470px;border-radius:40px 40px 0 0;background:linear-gradient(160deg,#f3f4f6 0%,#cfd6de 30%,#2f6cc0 60%,#1c4f96 100%)}

/* section headings */
.section-title{left:0;width:1200px;text-align:center;font-size:38px;font-weight:300;letter-spacing:.5px;color:var(--text)}
.section-title strong{font-weight:700;color:var(--blue)}
.section-title .green{font-weight:700;color:var(--green)}
.section-sub{left:0;width:1200px;text-align:center;font-size:15px;color:var(--text)}

/* feature items */
.feature{width:320px;text-align:center}
.feature svg{display:block;margin:0 auto}
.feature h3{margin-top:22px;font-size:19px;font-weight:600;color:var(--text)}
.feature p{margin:4px auto 0;width:250px;font-size:12px;line-height:17px;color:var(--muted)}
.on-green h3,.on-green p{color:var(--white)}
.on-green h3{font-size:19px;margin-top:20px}
.on-green p{font-size:12.5px;width:260px}

/* about */
.about-text{left:130px;top:1595px;width:580px;font-size:14px;line-height:24px;color:var(--muted)}
.about-text p+p{margin-top:16px}
.read-more{left:130px;top:1860px;width:128px;color:var(--text);font-size:14px}
.tablet-visual{left:735px;top:1550px;width:465px;height:380px;background:linear-gradient(150deg,#f4f5f7 0%,#dfe3e8 18%,#2f6cc0 35%,#1c4f96 100%);border-radius:30px 0 0 30px;transform:skewY(8deg)}

/* testimonials */
.testimonial{top:2742px;width:430px;display:flex;gap:22px}
.avatar{flex:0 0 88px;height:88px;border-radius:50%;background:linear-gradient(135deg,#c9a58d,#6b4e3d)}
.avatar.b{background:linear-gradient(135deg,#d7c2b0,#6e7a88)}
.quote{font-size:13px;font-style:italic;line-height:20px;color:var(--text)}
.who{margin-top:10px;font-size:17px;font-weight:700;color:var(--blue)}
.who span{font-size:13px;font-weight:400;color:var(--muted)}
.t-divider{left:600px;top:2742px;width:1px;height:110px;background:#d5d9dd}

/* contact */
.contact-title{left:130px;top:2982px;color:var(--white);font-size:38px;font-weight:300}
.contact-title strong{font-weight:700}
.contact-text{left:130px;top:3050px;width:440px;color:var(--white);font-size:14px;line-height:22px}
.field{position:absolute;background:var(--white);border:1px solid #c7d6e3;font-size:12px;color:var(--muted);padding:0 12px;display:flex;align-items:center}
.field.area{align-items:flex-start;padding-top:10px}
.submit{left:130px;top:3310px;width:120px;height:34px;background:var(--blue-dark);color:var(--white);font-size:13px;font-weight:700;display:flex;align-items:center;justify-content:center}
.map{left:600px;top:2872px;width:600px;height:523px;background:linear-gradient(140deg,#ece8e0,#dcd8cf)}
.map-card{left:735px;top:3018px;width:335px;height:172px;background:var(--green);color:var(--white);padding:22px 24px;font-size:14px}
.map-card .row{display:flex;gap:14px;align-items:flex-start}
.map-card .row+.row{margin-top:12px}
.map-card .addr{font-weight:700;font-size:15px;line-height:22px}
.map-pointer{left:1003px;top:3189px;width:0;height:0;border-left:14px solid transparent;border-right:14px solid transparent;border-top:16px solid var(--green)}

/* footer */
.footer-links{left:130px;top:3419px;display:flex;gap:14px;color:var(--white);font-size:13px}
.footer-links i{font-style:normal;opacity:.8}
.copyright{left:130px;top:3448px;color:var(--white);font-size:13px}
.social{left:868px;top:3414px;display:flex;gap:12px}
.social span{width:30px;height:30px;background:#4f7bb5}
.to-top{left:578px;top:3373px;width:44px;height:44px;border-radius:50%;background:var(--white);border:2px solid #c7d3df;display:flex;align-items:center;justify-content:center}
</style>
</head>
<body>
<div class="canvas">

  <svg class="bands" width="1200" height="3488" viewBox="0 0 1200 3488" aria-hidden="true">
    <defs>
      <linearGradient id="heroGrad" x1="0" y1="0" x2="1" y2="1">
        <stop offset="0" stop-color="#2a5f9f"/>
        <stop offset=".55" stop-color="#1c4d8d"/>
        <stop offset="1" stop-color="#4f86c0"/>
      </linearGradient>
      <linearGradient id="greenGrad" x1="0" y1="0" x2="1" y2="1">
        <stop offset="0" stop-color="#86c94a"/>
        <stop offset="1" stop-color="#6db835"/>
      </linearGradient>
    </defs>
    <polygon points="0,0 1200,0 1200,523 0,628" fill="url(#heroGrad)"/>
    <polygon points="0,814 1200,709 1200,1314 0,1384" fill="var(--grey-band)"/>
    <polygon points="0,2023 1200,1926 1200,2628 0,2709" fill="url(#greenGrad)"/>
    <rect x="0" y="2902" width="600" height="493" fill="var(--contact)"/>
    <rect x="0" y="3395" width="1200" height="93" fill="var(--footer)"/>
  </svg>

  <!-- header -->
  <div class="abs brand"><span class="brand-dot"></span>Brivel Marketing</div>
  <nav class="abs nav" style="left:0;width:1200px">
    <a class="active" style="left:638px">Home</a>
    <a style="left:720px">Features</a>
    <a style="left:818px">Pricing</a>
    <a style="left:905px">Contact Us</a>
    <a style="left:1015px">Skipper</a>
  </nav>

  <!-- hero -->
  <div class="abs hero-visual" role="img" aria-label="Hand holding a smartphone showing the Brivel Marketing app screen"></div>
  <h1 class="abs hero-title">Mobile Apps &amp;<br>Mobile Websites <span class="accent">Made easy!</span></h1>
  <p class="abs hero-text">BRIVELAPP.COM was built with small businesses in mind. Our goal is to help small businesses grow through affordable mobile marketing!</p>
  <div class="abs btn-outline login"><span class="lock"></span>Log in</div>

  <!-- welcome -->
  <h2 class="abs section-title" style="top:630px">WELCOME TO <span class="green">OUR BRIVEL INC</span></h2>
  <p class="abs section-sub" style="top:688px">We provide the easiest way for businesses to create Mobile Apps!</p>

  <!-- features -->
  <h2 class="abs section-title" style="top:812px">OUR <strong>FEATURES</strong></h2>
  <p class="abs section-sub" style="top:866px">Learn how Brivel benefits you</p>

  <div class="abs feature" style="left:80px;top:935px">
    <svg width="92" height="98" viewBox="0 0 92 98"><polygon points="46,3 88,27 88,71 46,95 4,71 4,27" fill="#fff" stroke="var(--green)" stroke-width="3"/><rect x="28" y="38" width="36" height="26" fill="#6cb6e0"/><path d="M46 22a9 9 0 0 1 9 9c0 7-9 15-9 15s-9-8-9-15a9 9 0 0 1 9-9z" fill="#e25b4b"/></svg>
    <h3>GPS Directions</h3><p>It is a long established fact that a of a page when looking at its layout.</p>
  </div>
  <div class="abs feature" style="left:440px;top:935px">
    <svg width="92" height="98" viewBox="0 0 92 98"><polygon points="46,3 88,27 88,71 46,95 4,71 4,27" fill="#fff" stroke="var(--green)" stroke-width="3"/><rect x="33" y="24" width="26" height="48" rx="4" fill="#3a4752"/><rect x="36" y="30" width="20" height="34" fill="#5ea9da"/></svg>
    <h3>One Touch Calling</h3><p>It is a long established fact that a of a page when looking at its layout.</p>
  </div>
  <div class="abs feature" style="left:798px;top:935px">
    <svg width="92" height="98" viewBox="0 0 92 98"><polygon points="46,3 88,27 88,71 46,95 4,71 4,27" fill="#fff" stroke="var(--green)" stroke-width="3"/><rect x="27" y="30" width="38" height="36" fill="#eef0f2" stroke="#9aa3ab"/><rect x="27" y="30" width="38" height="9" fill="#e25b4b"/><g fill="#9aa3ab"><rect x="32" y="44" width="6" height="5"/><rect x="43" y="44" width="6" height="5"/><rect x="54" y="44" width="6" height="5"/><rect x="32" y="54" width="6" height="5"/><rect x="43" y="54" width="6" height="5"/></g></svg>
    <h3>Event Listings Feature</h3><p>It is a long established fact that a of a page when looking at its layout.</p>
  </div>
  <div class="abs feature" style="left:80px;top:1138px">
    <svg width="92" height="98" viewBox="0 0 92 98"><polygon points="46,3 88,27 88,71 46,95 4,71 4,27" fill="#fff" stroke="var(--green)" stroke-width="3"/><rect x="30" y="30" width="32" height="38" fill="#fff" stroke="#555" stroke-width="2"/><g fill="#555"><rect x="34" y="34" width="9" height="9"/><rect x="49" y="34" width="9" height="9"/><rect x="34" y="55" width="9" height="9"/><rect x="49" y="49" width="4" height="4"/><rect x="54" y="57" width="4" height="6"/></g></svg>
    <h3>QR Coupons Feature</h3><p>It is a long established fact that a of a page when looking at its layout.</p>
  </div>
  <div class="abs feature" style="left:440px;top:1138px">
    <svg width="92" height="98" viewBox="0 0 92 98"><polygon points="46,3 88,27 88,71 46,95 4,71 4,27" fill="#fff" stroke="var(--green)" stroke-width="3"/><circle cx="38" cy="49" r="5" fill="#2b7bbf"/><circle cx="56" cy="38" r="5" fill="#2b7bbf"/><circle cx="56" cy="60" r="5" fill="#2b7bbf"/><path d="M38 49L56 38M38 49L56 60" stroke="#2b7bbf" stroke-width="3"/></svg>
    <h3>Social Share</h3><p>It is a long established fact that a of a page when looking at its layout.</p>
  </div>
  <div class="abs feature" style="left:798px;top:1138px">
    <svg width="92" height="98" viewBox="0 0 92 98"><polygon points="46,3 88,27 88,71 46,95 4,71 4,27" fill="#fff" stroke="var(--green)" stroke-width="3"/><rect x="30" y="26" width="32" height="44" rx="3" fill="#55636e"/><rect x="34" y="30" width="24" height="9" fill="#bfe3a5"/><g fill="#dfe4e8"><rect x="34" y="44" width="10" height="9"/><rect x="48" y="44" width="10" height="9"/><rect x="34" y="57" width="10" height="9"/><rect x="48" y="57" width="10" height="9"/></g></svg>
    <h3>Mortgage Calculator</h3><p>It is a long established fact that a of a page when looking at its layout.</p>
  </div>

  <!-- about -->
  <h2 class="abs section-title" style="top:1462px">ABOUT <strong>BRIVEL MARKETING</strong></h2>
  <p class="abs section-sub" style="top:1518px">Mobile Apps &amp; Mobile Websites From BRIVEL INC.</p>
  <div class="abs about-text">
    <p>It is a long established fact that a reader will be distracted by the readable content of a page when looking at its layout. The point of using Lorem Ipsum is that it has a more-or-less normal distribution of letters, as opposed to using 'Content here, content here', making it look like readable English.</p>
    <p>Many desktop publishing packages and web page editors now use Lorem Ipsum as their default model text, and a search for 'lorem ipsum' will uncover many web sites still in their infancy. Various versions have evolved over the years, sometimes by accident, sometimes on purpose.</p>
  </div>
  <div class="abs btn-outline read-more">Read More</div>
  <div class="abs tablet-visual" role="img" aria-label="Tablet showing the Brivel Marketing app screen"></div>

  <!-- creator -->
  <h2 class="abs section-title" style="top:2040px;color:var(--text)">MOBILE APP &amp; WEBSITE<strong style="color:var(--white)">CREATOR</strong></h2>
  <p class="abs section-sub" style="top:2094px;color:var(--white)">Mobile App &amp; Mobile Website Creator For Small Businesses.</p>

  <div class="abs feature on-green" style="left:80px;top:2172px">
    <svg width="92" height="98" viewBox="0 0 92 98"><polygon points="46,3 88,27 88,71 46,95 4,71 4,27" fill="#fff"/><rect x="28" y="32" width="36" height="26" fill="#2b5d9c"/><rect x="31" y="35" width="30" height="20" fill="#7ab8e6"/><rect x="40" y="60" width="12" height="4" fill="#2b5d9c"/></svg>
    <h3>Preview Online</h3><p>We allow you to preview your apps as we build it.</p>
  </div>
  <div class="abs feature on-green" style="left:440px;top:2172px">
    <svg width="92" height="98" viewBox="0 0 92 98"><polygon points="46,3 88,27 88,71 46,95 4,71 4,27" fill="#fff"/><rect x="30" y="46" width="8" height="20" fill="#2b5d9c"/><path d="M40 46l8-14c4 0 5 3 4 7l-1 5h11c3 0 4 3 3 5l-4 15H40z" fill="#4f86c0"/></svg>
    <h3>Incredibly Easy</h3><p>Our easy to use content manage system allows for beautiful app designs.</p>
  </div>
  <div class="abs feature on-green" style="left:798px;top:2172px">
    <svg width="92" height="98" viewBox="0 0 92 98"><polygon points="46,3 88,27 88,71 46,95 4,71 4,27" fill="#fff"/><rect x="30" y="28" width="32" height="42" fill="#3a4752"/><g fill="#cfd6dc"><rect x="34" y="33" width="24" height="5"/><rect x="34" y="42" width="24" height="5"/><rect x="34" y="51" width="24" height="5"/><rect x="34" y="60" width="24" height="5"/></g></svg>
    <h3>Powerful Hosting</h3><p>Our servers are hosted in the cloud using the latest hosting technology with 99.9% uptime for your apps.</p>
  </div>
  <div class="abs feature on-green" style="left:80px;top:2392px">
    <svg width="92" height="98" viewBox="0 0 92 98"><polygon points="46,3 88,27 88,71 46,95 4,71 4,27" fill="#fff"/><circle cx="50" cy="38" r="9" fill="#f2b33d"/><path d="M26 60h14l10 4 14-8c2 3 0 5-2 6l-14 8H26z" fill="#4f86c0"/></svg>
    <h3>Extremely Affordable</h3><p>Is more affordable than a newspaper ad and shows a huge return on investment for businesses.</p>
  </div>
  <div class="abs feature on-green" style="left:440px;top:2392px">
    <svg width="92" height="98" viewBox="0 0 92 98"><polygon points="46,3 88,27 88,71 46,95 4,71 4,27" fill="#fff"/><circle cx="42" cy="44" r="12" fill="none" stroke="#2b7bbf" stroke-width="7" stroke-dasharray="5 3"/><circle cx="42" cy="44" r="5" fill="#2b7bbf"/><path d="M52 54l12 12" stroke="#3a4752" stroke-width="5"/></svg>
    <h3>Customize Everything</h3><p>Customize every pixel inside your mobile apps within minutes using our pre-built designs or create your own.</p>
  </div>
  <div class="abs feature on-green" style="left:798px;top:2392px">
    <svg width="92" height="98" viewBox="0 0 92 98"><polygon points="46,3 88,27 88,71 46,95 4,71 4,27" fill="#fff"/><rect x="34" y="24" width="24" height="48" rx="4" fill="#3a4752"/><rect x="37" y="30" width="18" height="34" fill="#e25b4b"/></svg>
    <h3>Apps &amp; Websites</h3><p>We build and create native apps for iPhone, iPad, &amp; Android, and websites.</p>
  </div>

  <!-- testimonials -->
  <div class="abs testimonial" style="left:133px">
    <div class="avatar" role="img" aria-label="Portrait photo of Alan Preston"></div>
    <div>
      <p class="quote">" Lorem ipsum dolor sito amet contetur adipisco elit. Integer eu neque vel este feugiat sollicitudin semo aliu. Etiam convallis urna et suntie vulputate porta... "</p>
      <p class="who">Alan Preston, <span>CTO Portentus</span></p>
    </div>
  </div>
  <div class="abs t-divider"></div>
  <div class="abs testimonial" style="left:647px">
    <div class="avatar b" role="img" aria-label="Portrait photo of Neil Varga"></div>
    <div>
      <p class="quote">" Lorem ipsum dolor sito amet contetur adipisco elit. Integer eu neque vel este feugiat sollicitudin semo aliu. Etiam convallis urna et suntie vulputate porta... "</p>
      <p class="who">Neil Varga, <span>CTO Portentus</span></p>
    </div>
  </div>

  <!-- contact -->
  <div class="abs map" role="img" aria-label="Street map of the office neighbourhood"></div>
  <h2 class="abs contact-title">CONTACT <strong>FORM</strong></h2>
  <p class="abs contact-text">Simply dummy text of the printing and typesetting industry. standard dummy text ever since</p>
  <div class="field" style="left:130px;top:3124px;width:207px;height:35px">Your Name</div>
  <div class="field" style="left:347px;top:3124px;width:203px;height:35px">Your Email</div>
  <div class="field" style="left:130px;top:3168px;width:280px;height:35px">Web Site</div>
  <div class="field" style="left:420px;top:3168px;width:130px;height:35px">Budget $</div>
  <div class="field area" style="left:130px;top:3212px;width:420px;height:80px">Tell us about your company we love to learn!</div>
  <div class="abs submit">SUBMIT</div>

  <div class="abs map-card">
    <div class="row">
      <svg width="16" height="22" viewBox="0 0 16 22"><path d="M8 0a8 8 0 0 1 8 8c0 6-8 14-8 14S0 14 0 8a8 8 0 0 1 8-8z" fill="#fff"/><circle cx="8" cy="8" r="3" fill="var(--green)"/></svg>
      <p class="addr">Contrary to popular belief,<br>Lorem Ipsum,1234567</p>
    </div>
    <div class="row" style="margin-top:20px">
      <svg width="16" height="16" viewBox="0 0 16 16"><path d="M3 1l3 3-2 2c1 2 3 4 6 6l2-2 3 3-2 2C7 15 1 9 1 3z" fill="#fff"/></svg>
      <p>(555) 014 2290</p>
    </div>
    <div class="row">
      <svg width="16" height="12" viewBox="0 0 16 12"><rect width="16" height="12" fill="#fff"/><path d="M0 0l8 6 8-6" stroke="var(--green)" fill="none" stroke-width="1.5"/></svg>
      <p>info@brivelmarketing.com</p>
    </div>
  </div>
  <div class="abs map-pointer"></div>

  <!-- footer -->
  <div class="abs to-top"><svg width="16" height="10" viewBox="0 0 16 10"><path d="M2 8l6-6 6 6" stroke="#2c5a9b" stroke-width="2.5" fill="none"/></svg></div>
  <div class="abs footer-links"><span>Home</span><i>I</i><span>Features</span><i>I</i><span>Pricing</span><i>I</i><span>Contact Us</span><i>I</i><span>Skipper</span></div>
  <p class="abs copyright">Copyright © 2016 Brivel Marketing. All Rights Reserved.</p>
  <div class="abs social"><span></span><span></span><span></span><span></span><span></span></div>

</div>
</body>
</html>
```